Brightwell Support! Virtual Assistant business needs a Website

I have started an online business called "Brightwell Support". I offer all the same types of services as a typical Personal Assistant, only remotely. For example, document formatting and editing (word, powerpoint, excel etc.), email and calendar management, appointments and bookings, document creation, reports, travel and event management and so on.

I already have a logo ready to go, however I have yet to finalise the copy for the site, so if you could create the pages with pictures, and I can fill in the wording at a later date.

Target Market(s)

Anyone who is overloaded at work and needs someone to take the admin work off their hands.

Number of Pages Required

4 page

Font styles to use
Sans Serif
Script
Other font styles liked:
• Gotham Medium is used in my font

Colors

Designer to choose colors to be used in the design.

Requirements
Must have
• Home Page
• About Page
• Pricing Page
• Contact Page
Nice to have
• Pictures and a professional design, I like white space and simple design.
Should not have
• cartoons or anything unprofessional looking.

```html
<!DOCTYPE html>
<html lang="en">
<head>
<meta charset="utf-8">
<title>Brightwell Support – Virtual Assistant</title>
<link href="https://fonts.googleapis.com/css2?family=Montserrat:wght@300;400;500;600;700&display=swap" rel="stylesheet">
<style>
:root{
  --blue:#1d5ea8;
  --blue-dark:#17487f;
  --orange:#e8673a;
  --ink:#2d3440;
  --muted:#8a929d;
  --line:#dfe3e8;
  --band:#f3f4f6;
  --footer:#2e3440;
  --white:#ffffff;
}
*{box-sizing:border-box;margin:0;padding:0}
html,body{width:1200px;height:2488px;overflow:hidden;background:var(--white);font-family:"Montserrat",Arial,sans-serif;color:var(--ink)}
.page{position:relative;width:1200px;height:2488px}
.sec{position:absolute;left:0;width:1200px}

/* header */
.header{top:0;height:56px;background:var(--white);display:flex;align-items:center;justify-content:space-between;padding:0 160px}
.brand{display:flex;align-items:center;gap:10px;font-weight:700;font-size:19px;color:var(--blue);text-transform:uppercase;letter-spacing:.5px}
.brand-dot{width:30px;height:30px;border-radius:50%;background:var(--blue)}
.nav{display:flex;align-items:center;gap:30px;font-size:12px;color:var(--ink)}
.nav .active{color:var(--blue);border-bottom:2px solid var(--blue);padding-bottom:3px}
.btn{display:inline-block;font-size:11px;font-weight:500;padding:8px 22px;border-radius:2px;border:1px solid var(--blue);color:var(--blue);background:var(--white)}
.btn.solid{background:var(--blue);color:var(--white)}

/* hero */
.hero{top:56px;height:470px;background:linear-gradient(100deg,#6e757b 0%,#9aa1a5 45%,#d9dcdc 70%,#eef0ee 100%)}
.hero-photo{position:absolute;inset:0}
.hero-text{position:absolute;left:160px;top:118px;width:420px;color:var(--white)}
.hero-kicker{font-size:14px;font-weight:500}
.hero-title{font-size:34px;font-weight:600;margin:6px 0 14px}
.hero-copy{font-size:11px;line-height:1.6;opacity:.9}
.hero-actions{margin-top:18px;display:flex;gap:12px}
.btn.ghost{background:transparent;color:var(--white);border-color:var(--white)}
.btn.light{background:var(--white);color:var(--blue);border-color:var(--white)}

/* headings */
.heading{display:flex;align-items:center;justify-content:center;gap:18px;font-size:30px;font-weight:400}
.heading b{color:var(--blue);font-weight:600}
.heading::before,.heading::after{content:"";width:70px;height:1px;background:var(--line)}
.center{text-align:center}
.lead{font-size:11px;line-height:1.7;color:var(--muted)}

/* about */
.about{top:526px;height:380px}
.about-mark{width:54px;height:54px;border-radius:50%;background:var(--blue);margin:66px auto 12px}
.about .lead{width:720px;margin:14px auto 0}
.about .btn{margin-top:36px}

/* services */
.services{top:906px;height:330px;background:var(--band)}
.services-photo{position:absolute;left:160px;top:0;width:300px;height:290px;background:linear-gradient(135deg,#c9ced3,#8e969e 60%,#5b636c)}
.services-body{position:absolute;left:530px;top:40px;width:510px}
.services-body h2{font-size:30px;font-weight:400}
.services-body h2 b{color:var(--blue);font-weight:600}
.services-body .lead{margin:10px 0 14px}
.ticks{list-style:none;display:grid;grid-template-columns:1fr 1fr;gap:8px 20px;font-size:12px}
.ticks li{display:flex;align-items:center;gap:7px}
.ticks svg{flex:none}
.services-body .btn{margin-top:20px}

/* pricing */
.pricing{top:1236px;height:600px}
.pricing .heading{margin-top:120px}
.plans{position:absolute;left:240px;top:190px;width:720px;height:380px}
.plan{position:absolute;background:var(--band);text-align:center;padding-top:50px}
.plan.side{top:20px;width:230px;height:340px}
.plan.left{left:0}.plan.right{right:0}
.plan.featured{left:230px;top:0;width:260px;height:380px;background:var(--white);box-shadow:0 4px 24px rgba(0,0,0,.12);padding-top:40px}
.plan-name{font-size:9px;font-weight:600;text-transform:uppercase;letter-spacing:.5px}
.price{color:var(--orange);font-size:38px;font-weight:400;margin:16px 0 26px}
.price small{font-size:22px}
.plan.featured .price{font-size:48px}
.features{list-style:none;font-size:8px;line-height:2.1;text-transform:uppercase}
.features b{font-weight:700}
.plan .btn{margin-top:26px}

/* contact */
.contact{top:1836px;height:420px}
.contact .heading{font-size:30px;margin-top:20px}
.contact .heading::before,.contact .heading::after{display:none}
.contact .lead{width:520px;margin:10px auto 0}
.form{position:absolute;left:240px;top:130px;width:720px}
.fields{display:grid;grid-template-columns:repeat(3,1fr);gap:16px}
.field{height:26px;border:1px solid var(--line);font-size:9px;color:var(--muted);padding:7px 8px}
.field.area{height:110px;margin-top:14px}
.form .btn{display:block;width:128px;margin:42px auto 0;text-align:center}

/* footer */
.footer{top:2258px;height:230px;background:var(--footer);color:#c8ccd2}
.f-col{position:absolute;top:40px;font-size:10px;line-height:1.8}
.f-col h4{color:var(--blue);font-weight:600;font-size:14px;margin-bottom:6px}
.f-brand{left:160px;width:220px}
.f-links{left:480px}
.f-contact{left:660px;width:230px}
.socials{display:flex;gap:10px;margin-top:12px}
.socials span{width:18px;height:18px;border-radius:50%;background:#5b626e}
.to-top{position:absolute;left:980px;top:52px;width:34px;height:34px;border:1px solid var(--blue);border-radius:50%;display:flex;align-items:center;justify-content:center}
</style>
</head>
<body>
<div class="page">

  <header class="sec header">
    <div class="brand"><span class="brand-dot"></span>Brightwell Support</div>
    <nav class="nav">
      <span class="active">Home</span><span>About</span><span>Pricing</span><span>Contact</span>
      <span class="btn">Login</span>
    </nav>
  </header>

  <section class="sec hero">
    <div class="hero-photo" role="img" aria-label="Smiling assistant working at a laptop in a bright office"></div>
    <div class="hero-text">
      <p class="hero-kicker">I offer all the same types of services as a</p>
      <h1 class="hero-title">Typical Personal Assistant</h1>
      <p class="hero-copy">I take the everyday admin off your desk so you can focus on the work that matters. Reliable, discreet support delivered remotely, whenever you need it most.</p>
      <div class="hero-actions"><span class="btn light">Contact Us</span><span class="btn ghost">Get Started</span></div>
    </div>
  </section>

  <section class="sec about center">
    <div class="about-mark"></div>
    <h2 class="heading">About <b>Us</b></h2>
    <p class="lead">I am a dedicated virtual assistant helping busy professionals stay organised and on schedule. From inbox management to travel planning, I handle the detail so you can reclaim your time. Every task is completed with care, accuracy and complete confidentiality, giving you one dependable partner for all your administrative needs.</p>
    <span class="btn">Discover More</span>
  </section>

  <section class="sec services">
    <div class="services-photo" role="img" aria-label="Professional man working on a laptop at a desk"></div>
    <div class="services-body">
      <h2>Our <b>Services</b></h2>
      <p class="lead">Practical remote support for every part of your working day. Choose the services you need and I will tailor a plan that fits your workload and budget perfectly.</p>
      <ul class="ticks">
        <li><svg width="11" height="11" viewBox="0 0 11 11"><rect x=".5" y=".5" width="10" height="10" fill="none" stroke="#1d5ea8"/><path d="M2.5 5.5l2 2 4-4" fill="none" stroke="#1d5ea8" stroke-width="1.3"/></svg>Document Formatting and Editing</li>
        <li><svg width="11" height="11" viewBox="0 0 11 11"><rect x=".5" y=".5" width="10" height="10" fill="none" stroke="#1d5ea8"/><path d="M2.5 5.5l2 2 4-4" fill="none" stroke="#1d5ea8" stroke-width="1.3"/></svg>Document Creation</li>
        <li><svg width="11" height="11" viewBox="0 0 11 11"><rect x=".5" y=".5" width="10" height="10" fill="none" stroke="#1d5ea8"/><path d="M2.5 5.5l2 2 4-4" fill="none" stroke="#1d5ea8" stroke-width="1.3"/></svg>Email and Calendar Management</li>
        <li><svg width="11" height="11" viewBox="0 0 11 11"><rect x=".5" y=".5" width="10" height="10" fill="none" stroke="#1d5ea8"/><path d="M2.5 5.5l2 2 4-4" fill="none" stroke="#1d5ea8" stroke-width="1.3"/></svg>Reports</li>
        <li><svg width="11" height="11" viewBox="0 0 11 11"><rect x=".5" y=".5" width="10" height="10" fill="none" stroke="#1d5ea8"/><path d="M2.5 5.5l2 2 4-4" fill="none" stroke="#1d5ea8" stroke-width="1.3"/></svg>Appointments and Bookings</li>
        <li></li>
        <li><svg width="11" height="11" viewBox="0 0 11 11"><rect x=".5" y=".5" width="10" height="10" fill="none" stroke="#1d5ea8"/><path d="M2.5 5.5l2 2 4-4" fill="none" stroke="#1d5ea8" stroke-width="1.3"/></svg>Travel and Event Management</li>
      </ul>
      <span class="btn">Contact Us</span>
    </div>
  </section>

  <section class="sec pricing">
    <h2 class="heading">Pricing <b>Plans</b></h2>
    <div class="plans">
      <div class="plan side left">
        <p class="plan-name">Basic Plan</p>
        <p class="price">$ 29 <small>/ mo.</small></p>
        <ul class="features"><li><b>Up to 10</b> hrs/month</li><li><b>Email</b> support</li><li><b>Bookings</b> included</li></ul>
        <span class="btn">Get Started</span>
      </div>
      <div class="plan featured">
        <p class="plan-name">Standard Plan</p>
        <p class="price">$ 59 <small>/ mo.</small></p>
        <ul class="features"><li><b>Up to 25</b> hrs/month</li><li><b>Email</b> support</li><li><b>Bookings</b> included</li><li><b>Priority</b> response</li></ul>
        <span class="btn solid">Get Started</span>
      </div>
      <div class="plan side right">
        <p class="plan-name">Premium Plan</p>
        <p class="price">$ 199 <small>/ mo.</small></p>
        <ul class="features"><li><b>Up to 60</b> hrs/month</li><li><b>Email</b> support</li><li><b>Bookings</b> included</li></ul>
        <span class="btn">Get Started</span>
      </div>
    </div>
  </section>

  <section class="sec contact center">
    <h2 class="heading">How Can I <b>Help You Today?</b></h2>
    <p class="lead">Tell me a little about your workload and I will get back to you within one business day with ideas on how I can help.</p>
    <form class="form">
      <div class="fields"><div class="field">Name</div><div class="field">Email</div><div class="field">Phone</div></div>
      <div class="field area">Your Message</div>
      <span class="btn">Send Message</span>
    </form>
  </section>

  <footer class="sec footer">
    <div class="f-col f-brand">
      <h4>Brightwell Support</h4>
      <p>Remote administrative support for busy professionals.</p>
      <div class="socials"><span></span><span></span></div>
    </div>
    <div class="f-col f-links">
      <h4>Quick Links</h4>
      <p>Home<br>About<br>Pricing<br>Contact</p>
    </div>
    <div class="f-col f-contact">
      <h4>Contact</h4>
      <p>14 Harbour Lane, Brisbane QLD 4000<br>Call: +61 400 555 019<br>E: hello@brightwellsupport.com</p>
    </div>
    <div class="to-top"><svg width="12" height="12" viewBox="0 0 12 12"><path d="M2 8l4-4 4 4" fill="none" stroke="#1d5ea8" stroke-width="1.5"/></svg></div>
  </footer>

</div>
</body>
</html>
```